Business Card for TQM

We need a Corporate style business card for a new Industrial recycling company based in Australia. We recycle industrial products from Mining companies, power stations and other large industry all around the country.

We want the card to represent a modern, innovative professional company that is an industry leader.

We want the card to be double sided. I think with the logo centred by itself on one side and the text displayed with all our details on the other side.

(or you could put the persons name with the job title on the side with the logo?? I'll leave that up to your creative sides)

Open to how you divide and place the information on the one side of the card.

I think the persons name and the title should have its own place. The rest of the information can be placed as you think is best and then I will provide feedback as to what I think works best.

I have attached the logo file so you can add that to the one side. Whether you use it in a smaller form on the second side too is an option but I'll leave that up to you initially?

Information required on the card is as follows

Darren Pollock
Director

0428 917 306

darren@tqmv.com.au

Po Box 582
Brindle ACT 2611

www.tqmv.com.au

ACN 273 581 926 (This can be in very small print and can be in the bottom corner of the card or somewhere not very prominent
Updates

Wanted to thank everyone for their submissions. 

We were really torn on about 5 designs in the end.

We decided to go with the first one we liked.

We have another company that is going to need logo and business card design in the coming weeks.

I will save your designer ID's so I can invite you all to that project. too!

Thanks again and all the best

Darren

Target Market(s)

Corporate and medium to large business clients

Industry/Entity Type

Industrial

```html
<!DOCTYPE html>
<html lang="en">
<head>
<meta charset="utf-8">
<title>Total Quality Materials – Business Card</title>
<link rel="stylesheet" href="https://fonts.googleapis.com/css2?family=Arimo:wght@400;700&display=swap">
<style>
  :root {
    --page-bg: #e9e9e7;
    --card-dark: #1c1d1f;
    --card-dark-edge: #2a2c2f;
    --card-light: #ffffff;
    --ink: #1a1a1a;
    --accent-blue: #1f7fb6;
    --accent-green: #5fb832;
    --band-dark: #1f2022;
    --band-line: #2a74b8;
    --faint-mark: #cfe6c4;
    --logo-light: #f2f2f2;
    --logo-dark: #2c2f33;
  }
  * { box-sizing: border-box; margin: 0; padding: 0; }
  html, body {
    width: 1200px;
    height: 784px;
    overflow: hidden;
    background: var(--page-bg);
    font-family: "Arimo", Arial, sans-serif;
  }
  .canvas {
    position: relative;
    width: 1200px;
    height: 784px;
  }
  .card {
    position: absolute;
    top: 227px;
    width: 540px;
    height: 330px;
    border-radius: 4px;
    overflow: hidden;
    box-shadow: 0 6px 18px rgba(0,0,0,0.18);
  }

  /* Back side: logo centred on dark */
  .card--back {
    left: 50px;
    background: radial-gradient(ellipse at 40% 35%, var(--card-dark-edge) 0%, var(--card-dark) 70%);
    display: flex;
    align-items: center;
    justify-content: center;
  }
  .brand {
    display: flex;
    align-items: center;
    gap: 18px;
  }
  .brand__mark {
    flex: none;
    border-radius: 50%;
    background: var(--accent-green);
  }
  .brand__name {
    font-weight: 700;
    text-transform: uppercase;
    letter-spacing: 0.04em;
    line-height: 1.1;
  }
  .card--back .brand__mark { width: 96px; height: 96px; }
  .card--back .brand__name { font-size: 30px; color: var(--logo-light); }

  /* Front side: details */
  .card--front {
    left: 610px;
    background: var(--card-light);
  }
  .card--front .brand {
    position: absolute;
    left: 32px;
    top: 30px;
    gap: 14px;
  }
  .card--front .brand__mark { width: 64px; height: 64px; }
  .card--front .brand__name { font-size: 20px; color: var(--logo-dark); }

  .faint-mark {
    position: absolute;
    right: 28px;
    top: 60px;
    width: 170px;
    height: 170px;
    border-radius: 50%;
    background: var(--faint-mark);
    opacity: 0.35;
  }

  .person {
    position: absolute;
    left: 34px;
    top: 124px;
  }
  .person__name {
    font-size: 18px;
    font-weight: 700;
    color: var(--ink);
  }
  .person__title {
    font-size: 14px;
    color: var(--accent-blue);
    margin-top: 3px;
  }

  .contact {
    position: absolute;
    left: 34px;
    top: 172px;
    list-style: none;
    font-size: 16px;
    color: var(--ink);
  }
  .contact__item {
    display: flex;
    align-items: center;
    gap: 6px;
    height: 20px;
  }
  .contact__icon {
    width: 16px;
    height: 16px;
    flex: none;
    fill: var(--accent-green);
  }
  .contact__item--indent { padding-left: 22px; }

  .company-number {
    position: absolute;
    right: 22px;
    top: 268px;
    font-size: 11px;
    color: var(--ink);
    letter-spacing: 0.02em;
  }

  .footer-band {
    position: absolute;
    left: 0;
    right: 0;
    bottom: 0;
    height: 40px;
    background: var(--band-dark);
    border-top: 4px solid var(--band-line);
  }
</style>
</head>
<body>
<main class="canvas">

  <section class="card card--back" aria-label="Card back">
    <div class="brand">
      <span class="brand__mark" aria-hidden="true"></span>
      <span class="brand__name">Total Quality<br>Materials</span>
    </div>
  </section>

  <section class="card card--front" aria-label="Card front">
    <div class="faint-mark" aria-hidden="true"></div>

    <div class="brand">
      <span class="brand__mark" aria-hidden="true"></span>
      <span class="brand__name">Total Quality<br>Materials</span>
    </div>

    <div class="person">
      <p class="person__name">Darren Pollock</p>
      <p class="person__title">Director</p>
    </div>

    <ul class="contact">
      <li class="contact__item">
        <svg class="contact__icon" viewBox="0 0 16 16" aria-hidden="true"><path d="M3.2 1.5l2.3 0 1.2 3.3-1.6 1.1c.8 1.8 2.2 3.2 4 4l1.1-1.6 3.3 1.2v2.3c0 .9-.8 1.7-1.7 1.6C6.3 13 3 9.7 1.6 3.2 1.5 2.3 2.3 1.5 3.2 1.5z"/></svg>
        <span>0428 917 306</span>
      </li>
      <li class="contact__item">
        <svg class="contact__icon" viewBox="0 0 16 16" aria-hidden="true"><path d="M1 3h14v10H1z M2.2 4.2v.4L8 8.6l5.8-4v-.4z" fill-rule="evenodd"/></svg>
        <span>darren@tqmv.com.au</span>
      </li>
      <li class="contact__item">
        <svg class="contact__icon" viewBox="0 0 16 16" aria-hidden="true"><path d="M8 1a7 7 0 1 0 0 14A7 7 0 0 0 8 1zm0 1.4c.7 0 1.6 1.4 1.9 4.1H6.1C6.4 3.8 7.3 2.4 8 2.4zM2.5 6.5a5.6 5.6 0 0 1 2.6-3.3c-.4.9-.7 2-.8 3.3zm0 3h1.8c.1 1.3.4 2.4.8 3.3a5.6 5.6 0 0 1-2.6-3.3zM8 13.6c-.7 0-1.6-1.4-1.9-4.1h3.8c-.3 2.7-1.2 4.1-1.9 4.1zm2.9-.8c.4-.9.7-2 .8-3.3h1.8a5.6 5.6 0 0 1-2.6 3.3zm.8-6.3c-.1-1.3-.4-2.4-.8-3.3a5.6 5.6 0 0 1 2.6 3.3z"/></svg>
        <span>www.tqmv.com.au</span>
      </li>
      <li class="contact__item">
        <svg class="contact__icon" viewBox="0 0 16 16" aria-hidden="true"><path d="M8 1.5L1 7.8h2V14.5h3.8v-4h2.4v4H13V7.8h2z"/></svg>
        <span>Po Box 582</span>
      </li>
      <li class="contact__item contact__item--indent">
        <span>Brindle ACT 2611</span>
      </li>
    </ul>

    <p class="company-number">ACN 273 581 926</p>

    <div class="footer-band" aria-hidden="true"></div>
  </section>

</main>
</body>
</html>
```